Brimvale Crest Homes needs a business card

We need a business card for a new company in Canada, Ontario. Our company is all about luxury contraction homes for our clients. Our product and services are custom projects design. Under the business logo that will be created, we want a slogan that will be a memorable phrase for consumers to remember us to tell their friends and relatives.

Additional infomation
- Teodoro Vanlesky
- President / Ceo
-519.304.7718

Find point what luxury construction products and services can be done

We like to see colors:
- #663300
- and something other colors or color that would attract the client needs and wants

The final design should communicate leads from new or old clients that will grow our empire. Most of all, we try to work among the budget that clients want

NOTE
- we also need an icon for the business (Example: Instagram, Facebook, and Whatsapp icons)
- We want the company name to be remembered easily for clients and our distributors who would get our orders.
- we need an icon on the business cards: Facebook and Instagram.

Thanks,
Brimvale Crest Homes

```html
<!DOCTYPE html>
<html lang="en">
<head>
<meta charset="utf-8">
<title>Brimvale Crest Homes — Business Card</title>
<link rel="stylesheet" href="https://fonts.googleapis.com/css2?family=Cinzel:wght@400;600&family=Cormorant+Garamond:ital,wght@0,500;0,600;1,600&display=swap">
<style>
  :root {
    --brown: #663300;
    --grey: #b8b8bc;
    --white: #ffffff;
    --ink: #1c0e02;
    --stage: #2b2b2d;
  }
  * { margin: 0; padding: 0; box-sizing: border-box; }
  html, body { width: 1200px; height: 900px; overflow: hidden; background: var(--stage); }
  .canvas { position: relative; width: 1200px; height: 900px; }

  .card {
    position: absolute; width: 620px; height: 354px; overflow: hidden;
    box-shadow: 0 14px 30px rgba(0,0,0,.45);
  }
  .card svg.shape { position: absolute; inset: 0; }

  /* Front */
  .card-front { left: 60px; top: 70px; background: var(--brown); }
  .card-front .base-band { position: absolute; left: 0; right: 0; bottom: 0; height: 40px; background: var(--grey); }
  .map-area {
    position: absolute; left: 110px; top: 50px; width: 420px; height: 230px; border-radius: 50%;
    background: radial-gradient(ellipse at center, rgba(140,80,30,.55), rgba(102,51,0,0) 70%);
  }
  .brand-lockup {
    position: absolute; left: 0; right: 0; top: 128px;
    display: flex; align-items: center; justify-content: center; gap: 14px;
    font-family: "Cinzel", serif; font-weight: 600; font-size: 38px; letter-spacing: 1px; color: var(--white);
    white-space: nowrap;
  }
  .brand-dot { width: 16px; height: 16px; border-radius: 50%; background: var(--white); }
  .brand-services {
    position: absolute; left: 50%; top: 188px; transform: translateX(-50%);
    background: var(--white); color: var(--brown); padding: 2px 12px;
    font-family: "Cormorant Garamond", serif; font-weight: 600; font-size: 17px; white-space: nowrap;
  }
  .slogan {
    position: absolute; left: 0; right: 0; top: 262px; display: flex; align-items: center; justify-content: center; gap: 14px;
    font-family: "Cormorant Garamond", serif; font-style: italic; font-weight: 600; font-size: 21px; color: var(--ink);
    white-space: nowrap;
  }
  .slogan .rule { width: 60px; height: 2px; background: var(--ink); }

  /* Back */
  .card-back { left: 520px; top: 470px; background: var(--white); }
  .back-mark {
    position: absolute; left: 0; right: 0; top: 56px;
    display: flex; align-items: center; justify-content: center; gap: 10px;
    font-family: "Cinzel", serif; font-weight: 600; font-size: 24px; color: var(--brown); white-space: nowrap;
  }
  .contact {
    position: absolute; left: 200px; top: 222px; display: flex; align-items: center; gap: 16px; color: var(--white);
  }
  .person { text-align: right; font-family: "Cormorant Garamond", serif; font-weight: 600; white-space: nowrap; }
  .person-name { font-size: 21px; }
  .person-title { font-size: 18px; }
  .divider { width: 2px; height: 60px; background: var(--white); }
  .phone { display: flex; align-items: center; gap: 8px; font-family: "Cormorant Garamond", serif; font-weight: 600; font-size: 22px; white-space: nowrap; }
  .social { display: flex; gap: 6px; margin-top: 6px; }
  .social span { width: 16px; height: 16px; border-radius: 3px; background: var(--white); opacity: .85; }
  .services {
    position: absolute; left: 0; right: 0; bottom: 0; height: 38px; background: var(--grey);
    display: flex; align-items: center; justify-content: center; gap: 20px; list-style: none;
    font-family: "Cormorant Garamond", serif; font-weight: 600; font-size: 17px; color: var(--white);
    white-space: nowrap;
  }
  .services li { display: flex; align-items: center; gap: 6px; }
  .services li::before { content: ""; width: 10px; height: 10px; background: var(--brown); }
</style>
</head>
<body>
<main class="canvas">

  <section class="card card-front">
    <div class="map-area" role="img" aria-label="Faint dotted world map behind the brand name"></div>
    <div class="brand-lockup"><span class="brand-dot"></span>Brimvale Crest Homes</div>
    <div class="brand-services">Home Renovations | Custom Project Design</div>
    <div class="slogan"><span class="rule"></span>Helping you to find Home of your dreams<span class="rule"></span></div>
    <div class="base-band"></div>
  </section>

  <section class="card card-back">
    <svg class="shape" viewBox="0 0 620 354" aria-hidden="true">
      <path d="M0 300 Q 260 130 620 120 L 620 354 L 0 354 Z" fill="#663300"/>
      <path d="M130 310 Q 330 150 620 112 Q 340 170 140 306 Z" fill="#b8b8bc"/>
    </svg>
    <div class="back-mark">Brimvale Crest Homes</div>
    <div class="contact">
      <div class="person">
        <div class="person-name">Teodoro Vanlesky</div>
        <div class="person-title">President / Ceo</div>
      </div>
      <div class="divider"></div>
      <div>
        <div class="phone">
          <svg width="18" height="14" viewBox="0 0 18 14" aria-hidden="true"><path d="M1 4 Q9 -1 17 4 L15 6 L12 5 L12 3 Q9 2 6 3 L6 5 L3 6 Z M4 7 L14 7 L16 13 L2 13 Z" fill="#ffffff"/></svg>
          519.304.7718
        </div>
        <div class="social" aria-label="Social media links"><span></span><span></span><span></span></div>
      </div>
    </div>
    <ul class="services">
      <li>Roofing</li><li>Gutters</li><li>Wall Designing</li><li>Attic Ventilation</li><li>Pressure Washing</li>
    </ul>
  </section>

</main>
</body>
</html>
```